film festival poster

We need a poster designed for our film festival. It is called the Open Horizon Cinema Gathering www.openhorizoncinema.example This is a film festival about what it means to be free. We want the image to be bold and different, and yet speak about film and the importance of being a free human being. Maybe a combination of images that make up a bigger image?

```html
<!DOCTYPE html>
<html lang="en">
<head>
<meta charset="utf-8">
<title>Open Horizon Cinema Gathering — Poster</title>
<link rel="stylesheet" href="https://fonts.googleapis.com/css2?family=Yellowtail&family=Arimo:wght@700&display=swap">
<style>
  :root {
    --ink-navy: #1b1d3a;
    --teal: #3fb8a8;
    --peach: #f2d2bc;
    --violet: #7a3fb0;
    --lilac: #d9c4f0;
    --leaf: #3fae3a;
    --sun: #f0d23a;
    --crimson: #b01e4a;
    --title-pink: #e8208f;
    --title-shadow: rgba(60, 0, 30, 0.55);
    --paper: #ffffff;
  }
  html, body {
    margin: 0;
    padding: 0;
    width: 856px;
    height: 1200px;
    overflow: hidden;
    background: var(--paper);
  }
  .poster {
    position: relative;
    width: 856px;
    height: 1200px;
    overflow: hidden;
    background: var(--paper);
  }
  .poster__artwork {
    position: absolute;
    inset: 0;
    background:
      radial-gradient(ellipse 260px 340px at 150px 300px, var(--ink-navy) 0%, rgba(27,29,58,0.85) 45%, rgba(27,29,58,0) 100%),
      radial-gradient(ellipse 220px 200px at 560px 120px, rgba(27,29,58,0.8) 0%, rgba(27,29,58,0) 100%),
      radial-gradient(ellipse 200px 180px at 760px 90px, var(--teal) 0%, rgba(63,184,168,0) 100%),
      radial-gradient(ellipse 160px 140px at 820px 480px, var(--crimson) 0%, rgba(176,30,74,0) 100%),
      radial-gradient(ellipse 130px 110px at 810px 560px, var(--sun) 0%, rgba(240,210,58,0) 100%),
      radial-gradient(ellipse 320px 360px at 600px 600px, var(--peach) 0%, rgba(242,210,188,0.9) 50%, rgba(242,210,188,0) 100%),
      radial-gradient(ellipse 260px 220px at 200px 1050px, var(--violet) 0%, rgba(122,63,176,0) 100%),
      radial-gradient(ellipse 180px 160px at 260px 960px, var(--teal) 0%, rgba(63,184,168,0) 100%),
      radial-gradient(ellipse 200px 180px at 470px 880px, var(--leaf) 0%, rgba(63,174,58,0) 100%),
      radial-gradient(ellipse 120px 120px at 440px 1050px, var(--sun) 0%, rgba(240,210,58,0) 100%),
      radial-gradient(ellipse 240px 200px at 380px 180px, rgba(63,184,168,0.5) 0%, rgba(63,184,168,0) 100%),
      linear-gradient(160deg, var(--lilac) 0%, var(--peach) 55%, var(--lilac) 100%);
  }
  .poster__title {
    position: absolute;
    left: 0;
    top: 0;
    width: 856px;
    height: 1200px;
    margin: 0;
    font-family: "Yellowtail", cursive;
    font-weight: 400;
    color: var(--title-pink);
    text-shadow: 4px 5px 4px var(--title-shadow);
    pointer-events: none;
  }
  .poster__title-line {
    position: absolute;
    white-space: nowrap;
    font-size: 118px;
    line-height: 1;
    transform-origin: left center;
    transform: rotate(-24deg);
  }
  .poster__title-line--first  { left: 80px;  top: 470px; }
  .poster__title-line--second { left: 150px; top: 590px; }
  .poster__title-line--third  { left: 100px; top: 820px; transform: rotate(-28deg); }
  .poster__brand {
    position: absolute;
    right: 24px;
    bottom: 22px;
    display: flex;
    flex-direction: column;
    align-items: flex-end;
    font-family: "Arimo", Arial, sans-serif;
    font-weight: 700;
    color: var(--paper);
  }
  .poster__brand-name {
    display: flex;
    align-items: center;
    gap: 10px;
    font-size: 44px;
    line-height: 1;
    letter-spacing: -1px;
  }
  .poster__brand-dot {
    width: 16px;
    height: 16px;
    border-radius: 50%;
    background: var(--paper);
  }
  .poster__brand-url {
    margin-top: 12px;
    font-size: 14px;
    letter-spacing: 0.2px;
  }
</style>
</head>
<body>
  <main class="poster">
    <div class="poster__artwork" role="img" aria-label="Abstract collage of blended film imagery in navy, teal, peach, violet, green and magenta tones"></div>
    <h1 class="poster__title">
      <span class="poster__title-line poster__title-line--first">Open Horizon</span>
      <span class="poster__title-line poster__title-line--second">Cinema</span>
      <span class="poster__title-line poster__title-line--third">Gathering</span>
    </h1>
    <footer class="poster__brand">
      <div class="poster__brand-name"><span class="poster__brand-dot"></span>Open Horizon</div>
      <div class="poster__brand-url">www.openhorizoncinema.example</div>
    </footer>
  </main>
</body>
</html>
```